Quality Improvement Software for healthcare agencies needs a website.

Veltrix820 is a software for hospices and home health agencies to manage their Quality Assurance Performance Improvement programs to remain complaint with the standards set by Sanovia and the Bureau of Civic Wellbeing. The web accessible software-as-a-service provides an easy, turn-key way for agencies to organize all the information they need to manage and track.

Coded - Design and coding required

4 page

```html
<!DOCTYPE html>
<html lang="en">
<head>
<meta charset="utf-8">
<title>Veltrix820 – Quality Improvement Software for Healthcare</title>
<link href="https://fonts.googleapis.com/css2?family=Poppins:wght@300;400;500;600;700&display=swap" rel="stylesheet">
<style>
:root{
  --navy:#1c2d4e;
  --navy-deep:#172644;
  --blue:#2aa8e8;
  --blue-soft:#e7f4fc;
  --orange:#f4921f;
  --text:#2b2f3a;
  --muted:#6b7280;
  --line:#e6e8ee;
  --white:#ffffff;
}
*{box-sizing:border-box;margin:0;padding:0}
html,body{width:1200px;height:4812px;overflow:hidden}
body{position:relative;font-family:'Poppins',sans-serif;color:var(--text);background:var(--white)}
.abs{position:absolute}
.btn{position:absolute;display:flex;align-items:center;justify-content:center;border-radius:20px;font-size:11px;font-weight:500;color:var(--white);background:var(--navy)}
.btn-blue{background:var(--blue)}
.btn-outline{background:transparent;border:1.5px solid var(--white)}
.photo{position:absolute;overflow:hidden}
.card{position:absolute;background:var(--white);border-radius:10px;box-shadow:0 6px 20px rgba(20,30,60,.14)}

/* header */
.site-header{position:absolute;left:0;top:0;width:1200px;height:112px;background:var(--white)}
.brand{position:absolute;display:flex;align-items:center;gap:10px;font-weight:700;color:var(--navy)}
.brand-mark{width:22px;height:22px;background:var(--blue);border-radius:4px}
.site-header .brand{left:131px;top:40px;font-size:32px}
.nav{position:absolute;top:54px;font-size:11px;color:var(--text)}
.nav.active{color:var(--blue);font-weight:500}
.header-cta{left:905px;top:45px;width:131px;height:32px;justify-content:flex-start;padding-left:16px;gap:16px}

/* hero */
.hero{position:absolute;left:0;top:112px;width:1200px;height:580px;background:linear-gradient(90deg,#27b0ec 0%,#4eaadb 40%,#e9a04a 75%,#f48f1c 100%);overflow:hidden}
.hero-photo{left:610px;top:0;width:560px;height:580px;border-radius:280px 0 0 0;background:radial-gradient(circle at 55% 40%,#f1d9c5 0%,#d4a98b 35%,#8aa9b9 70%,#5d93b3 100%);opacity:.92}
.hero-wave{position:absolute;left:0;bottom:0;width:1200px;height:140px}
.hero-kicker{left:137px;top:288px;font-size:13px;font-weight:500;color:var(--white);letter-spacing:.3px}
.hero-title{left:137px;top:310px;font-size:44px;line-height:53px;font-weight:500;color:var(--white);letter-spacing:1px}
.hero-text{left:137px;top:424px;width:340px;font-size:11px;line-height:18px;color:var(--white)}
.hero-cta{left:138px;top:478px;width:135px;height:32px}
.pager{left:1157px;top:382px;font-size:10px;color:var(--navy);display:flex;align-items:center;gap:6px}
.pager span{display:block;width:24px;height:2px;background:var(--navy)}
.card-title{font-size:11px;font-weight:600;color:var(--navy)}

/* about */
.about-photo{left:140px;top:766px;width:402px;height:378px;border-radius:0 0 40px 160px;background:linear-gradient(160deg,#eef1f4 0%,#cdd6de 45%,#9fb0c0 100%)}
.eyebrow{font-size:14px;font-weight:500;color:var(--orange)}
.h-section{font-size:38px;font-weight:600;color:var(--navy)}
.body-text{font-size:11px;line-height:15px;color:var(--text)}
.sub-title{font-size:14px;font-weight:600;color:var(--navy)}

/* solutions */
.center{text-align:center}
.solution-img{top:1340px;width:279px;height:267px;border-radius:6px}
.solution-name{top:1636px;width:279px;font-size:24px;font-weight:500;color:var(--navy);text-align:center}
.solution-desc{top:1677px;width:279px;font-size:10.5px;line-height:15px;color:var(--muted);text-align:center}

/* features */
.features{left:0;top:1877px;width:1200px;height:585px;background:var(--navy)}
.features-photo{left:120px;top:1965px;width:470px;height:470px;border-radius:50%;background:radial-gradient(circle at 50% 45%,#c9a27a 0%,#b08560 55%,#8d6a4c 100%)}
.feature-item{position:absolute;display:flex;align-items:flex-start;gap:10px;font-size:13px;color:var(--white);line-height:17px}
.tick{flex:none;width:17px;height:17px}

/* video */
.video{left:161px;top:2673px;width:875px;height:424px;background:linear-gradient(120deg,#d9dde3 0%,#f2f3f5 40%,#c7ced7 75%,#8f9caa 100%)}

/* testimonials */
.quote-card{top:3262px;width:275px;height:220px;padding:22px 28px}
.avatar{width:64px;height:64px;border-radius:50%;background:linear-gradient(135deg,#9db7cf,#4e6d8c)}
.quote-mark{position:absolute;right:22px;top:-14px;font-size:70px;font-weight:700;color:var(--blue);line-height:1;font-style:normal}
.stars{color:var(--orange);font-size:11px;letter-spacing:2px}

/* blog */
.blog-card{top:3660px;width:278px;height:362px;border-radius:8px;overflow:hidden}
.blog-img{left:0;top:0;width:278px;height:194px}
.date{position:absolute;left:30px;top:160px;width:50px;height:46px;background:var(--blue);color:var(--white);font-size:11px;line-height:14px;text-align:center;padding-top:9px}

/* contact */
.field{position:absolute;background:#f1f2f5;border-radius:6px;font-size:10px;color:#8a8f99;padding:8px 14px}

/* footer */
.footer{left:0;top:4420px;width:1200px;height:337px}
.foot-h{font-size:15px;font-weight:500;color:var(--white)}
.foot-h::after{content:"";display:block;width:38px;height:2px;background:var(--white);margin-top:6px}
.foot-list{list-style:none;font-size:11px;color:var(--white);line-height:19px}
.social{position:absolute;top:4774px;width:26px;height:26px;border-radius:50%;background:var(--blue)}
</style>
</head>
<body>

<header class="site-header">
  <div class="brand"><span class="brand-mark"></span>Veltrix820</div>
  <div class="nav active" style="left:462px">Home</div>
  <div class="nav" style="left:529px">About us</div>
  <div class="nav" style="left:609px">Our Services</div>
  <div class="nav" style="left:710px">Features</div>
  <div class="nav" style="left:789px">Contact us</div>
  <div class="btn header-cta">Get Started
    <svg width="34" height="12" viewBox="0 0 34 12"><circle cx="26" cy="6" r="9" fill="#2aa8e8"/><path d="M2 6h28M25 2l5 4-5 4" stroke="#fff" stroke-width="1.6" fill="none"/></svg>
  </div>
</header>

<section class="hero">
  <div class="photo hero-photo" role="img" aria-label="Smiling caregiver hugging an elderly woman"></div>
  <svg class="hero-wave" viewBox="0 0 1200 140" preserveAspectRatio="none"><path d="M0 140V128C150 80 300 30 480 60S800 150 1200 100V140Z" fill="#fff"/></svg>
</section>
<div class="abs hero-kicker">QUALITY IMPROVEMENT</div>
<h1 class="abs hero-title">SOFTWARE FOR<br>HEALTHCARE</h1>
<p class="abs hero-text">Lorem Ipsum is simply dummy industryprintingindustry lorem since standard the 1500s.</p>
<div class="btn hero-cta">Get Started</div>
<div class="abs pager">02 <span></span></div>

<div class="card" style="left:994px;top:198px;width:139px;height:152px;padding:12px">
  <div class="card-title" style="text-align:center">Data Tables</div>
  <svg width="115" height="110" viewBox="0 0 115 110" style="margin-top:6px">
    <circle cx="57" cy="52" r="42" fill="#2aa8e8"/>
    <path d="M57 52V10A42 42 0 0 1 98 45Z" fill="#f4921f"/>
    <path d="M57 52L98 45A42 42 0 0 1 86 82Z" fill="#f6c229"/>
    <path d="M57 52L86 82A42 42 0 0 1 48 93Z" fill="#1c2d4e"/>
    <path d="M57 52L48 93A42 42 0 0 1 20 72Z" fill="#e4572e"/>
  </svg>
</div>
<div class="card" style="left:518px;top:458px;width:159px;height:101px;padding:12px 14px">
  <div class="card-title">Graph</div>
  <div style="font-size:17px;font-weight:600;color:var(--navy);margin-top:12px">8,726</div>
  <div style="font-size:9px;color:#e4572e">+ 19,74%</div>
  <svg class="abs" style="left:78px;top:36px" width="68" height="40" viewBox="0 0 68 40"><path d="M0 34 12 28 22 30 32 20 42 22 54 10 66 4" stroke="#f4921f" stroke-width="1.6" fill="none"/></svg>
</div>
<div class="card" style="left:632px;top:604px;width:175px;height:99px;padding:12px 16px">
  <div class="card-title">Charts</div>
  <div style="font-size:8.5px;color:var(--muted);margin-top:4px">Monthly Progress</div>
  <div style="margin-top:10px;display:flex;gap:6px;align-items:center"><span style="width:8px;height:8px;border-radius:50%;background:#e4572e"></span><span style="width:30px;height:3px;background:#dde"></span><span style="width:30px;height:3px;background:#dde"></span></div>
  <svg class="abs" style="left:116px;top:32px" width="40" height="40" viewBox="0 0 40 40"><circle cx="20" cy="20" r="15" stroke="#eee" stroke-width="5" fill="none"/><circle cx="20" cy="20" r="15" stroke="#f6c229" stroke-width="5" fill="none" stroke-dasharray="70 95" transform="rotate(-90 20 20)"/><text x="20" y="23" font-size="8" text-anchor="middle" fill="#1c2d4e" font-family="Poppins,sans-serif">75%</text></svg>
</div>

<section>
  <div class="photo about-photo" role="img" aria-label="Doctor reviewing a clipboard with an older couple"></div>
  <div class="abs eyebrow" style="left:607px;top:806px">About us</div>
  <h2 class="abs h-section" style="left:607px;top:826px">Veltrix820</h2>
  <p class="abs body-text" style="left:607px;top:887px;width:410px">Lorem Ipsum is simply dummy text of the printing and typesetting industry. Lorem Ipsum has been the industry's standard dummy text ever since the 1500s, when an unknown printer took a galley of type and scrambled it to make a type specimen book. It has survived not only five centuries, but also the leap into electronic typesetting,remaining essentially unchanged.</p>
  <div class="abs sub-title" style="left:607px;top:992px">Easy Integration</div>
  <p class="abs body-text" style="left:607px;top:1015px;width:195px">Lorem Ipsum is simply dummy of the printing and typesetting industry. Lorem Ipsum</p>
  <div class="abs sub-title" style="left:820px;top:992px">Real-time Analytics</div>
  <p class="abs body-text" style="left:820px;top:1015px;width:195px">Lorem Ipsum is simply dummy of the printing and typesetting industry. Lorem Ipsum</p>
  <div class="btn" style="left:607px;top:1086px;width:135px;height:30px">Read More</div>
</section>

<section>
  <h2 class="abs center" style="left:0;top:1252px;width:1200px;font-size:38px;font-weight:500;color:var(--navy);letter-spacing:.5px">Healthcare &amp; Medical Solutions</h2>
  <div class="abs center" style="left:0;top:1308px;width:1200px;font-size:11px;color:var(--text)">Quality Improvement Programs</div>
  <div class="photo solution-img" style="left:151px;background:linear-gradient(135deg,#dfe5ee,#8aa2c8 60%,#3b5ea8)" role="img" aria-label="Hands drawing charts on printed reports"></div>
  <div class="photo solution-img" style="left:478px;background:linear-gradient(135deg,#c9d4de,#7d94ad 60%,#3f5570)" role="img" aria-label="Nurse working at a computer"></div>
  <div class="photo solution-img" style="left:804px;background:linear-gradient(135deg,#eef0f3,#b9c1cc 55%,#e58a3a)" role="img" aria-label="Printed graphs with a colourful pie chart"></div>
  <div class="photo solution-img" style="left:1131px;background:linear-gradient(135deg,#d7dde4,#8ea3b5)" role="img" aria-label="Doctors reviewing data"></div>
  <div class="abs solution-name" style="left:151px">Creates Charts</div>
  <div class="abs solution-name" style="left:478px">Data Table</div>
  <div class="abs solution-name" style="left:804px">Graphs</div>
  <div class="abs solution-name" style="left:1131px;text-align:left;padding-left:36px">Events</div>
  <p class="abs solution-desc" style="left:151px">Lorem Ipsum is simply dummy text<br>of the printing and typesetting</p>
  <p class="abs solution-desc" style="left:478px">Lorem Ipsum is simply dummy text<br>of the printing and typesetting</p>
  <p class="abs solution-desc" style="left:804px">Lorem Ipsum is simply dummy text<br>of the printing and typesetting</p>
  <p class="abs solution-desc" style="left:1131px;text-align:left;padding-left:32px">Lorem<br>of th</p>
  <div class="btn" style="left:535px;top:1759px;width:134px;height:32px">View More</div>
</section>

<section>
  <div class="abs features"></div>
  <div class="photo features-photo" role="img" aria-label="Nurse with stethoscope holding a laptop"></div>
  <div class="card" style="left:93px;top:2043px;width:122px;height:116px;padding:14px">
    <svg width="94" height="70" viewBox="0 0 94 70"><path d="M12 50A35 35 0 0 1 82 50" stroke="#e6eef6" stroke-width="12" fill="none"/><path d="M12 50A35 35 0 0 1 60 17" stroke="#2aa8e8" stroke-width="12" fill="none"/><circle cx="47" cy="50" r="6" stroke="#1c2d4e" stroke-width="2" fill="none"/><rect x="18" y="64" width="58" height="3" fill="#dde"/></svg>
  </div>
  <div class="card" style="left:510px;top:2039px;width:54px;height:54px;display:flex;align-items:center;justify-content:center">
    <span style="width:24px;height:24px;background:var(--blue);border-radius:4px"></span>
  </div>
  <div class="card" style="left:112px;top:2310px;width:172px;height:120px;padding:10px 12px">
    <div class="card-title">Graph</div>
    <svg width="148" height="88" viewBox="0 0 148 88"><g fill="#2aa8e8"><rect x="22" y="50" width="6" height="30"/><rect x="48" y="30" width="6" height="50"/><rect x="74" y="44" width="6" height="36"/><rect x="100" y="20" width="6" height="60"/></g><g fill="#f4921f"><rect x="30" y="60" width="6" height="20"/><rect x="56" y="40" width="6" height="40"/><rect x="82" y="54" width="6" height="26"/><rect x="108" y="36" width="6" height="44"/></g><path d="M14 80H140M14 10V80" stroke="#ccd" stroke-width="1"/><path d="M20 56 50 40 76 52 104 24 130 34" stroke="#e4572e" stroke-width="1.4" fill="none"/></svg>
  </div>
  <h2 class="abs" style="left:673px;top:2004px;font-size:40px;font-weight:600;color:var(--white);letter-spacing:1.5px">Key Features</h2>
  <p class="abs body-text" style="left:673px;top:2068px;width:425px;color:var(--white)">Lorem Ipsum is simply dummy text of the printing and typesetting industry. Lorem Ipsum has been the industry's standard dummy text ever since the 1500s,</p>
  <div class="feature-item" style="left:673px;top:2142px"><svg class="tick" viewBox="0 0 17 17"><circle cx="8.5" cy="8.5" r="7.5" stroke="#2aa8e8" stroke-width="1.4" fill="none"/><path d="M5 8.7l2.5 2.5 4.5-5" stroke="#2aa8e8" stroke-width="1.6" fill="none"/></svg>Closing The Loop</div>
  <div class="feature-item" style="left:673px;top:2178px"><svg class="tick" viewBox="0 0 17 17"><circle cx="8.5" cy="8.5" r="7.5" stroke="#2aa8e8" stroke-width="1.4" fill="none"/><path d="M5 8.7l2.5 2.5 4.5-5" stroke="#2aa8e8" stroke-width="1.6" fill="none"/></svg>Identifying an issue,</div>
  <div class="feature-item" style="left:673px;top:2215px"><svg class="tick" viewBox="0 0 17 17"><circle cx="8.5" cy="8.5" r="7.5" stroke="#2aa8e8" stroke-width="1.4" fill="none"/><path d="M5 8.7l2.5 2.5 4.5-5" stroke="#2aa8e8" stroke-width="1.6" fill="none"/></svg>implementing solution</div>
  <div class="feature-item" style="left:673px;top:2251px"><svg class="tick" viewBox="0 0 17 17"><circle cx="8.5" cy="8.5" r="7.5" stroke="#2aa8e8" stroke-width="1.4" fill="none"/><path d="M5 8.7l2.5 2.5 4.5-5" stroke="#2aa8e8" stroke-width="1.6" fill="none"/></svg>Reevaluating for improvement.</div>
  <div class="feature-item" style="left:918px;top:2142px"><svg class="tick" viewBox="0 0 17 17"><circle cx="8.5" cy="8.5" r="7.5" stroke="#2aa8e8" stroke-width="1.4" fill="none"/><path d="M5 8.7l2.5 2.5 4.5-5" stroke="#2aa8e8" stroke-width="1.6" fill="none"/></svg>Reviewing Data</div>
  <div class="feature-item" style="left:918px;top:2178px"><svg class="tick" viewBox="0 0 17 17"><circle cx="8.5" cy="8.5" r="7.5" stroke="#2aa8e8" stroke-width="1.4" fill="none"/><path d="M5 8.7l2.5 2.5 4.5-5" stroke="#2aa8e8" stroke-width="1.6" fill="none"/></svg>Identifying Problem</div>
  <div class="feature-item" style="left:918px;top:2215px"><svg class="tick" viewBox="0 0 17 17"><circle cx="8.5" cy="8.5" r="7.5" stroke="#2aa8e8" stroke-width="1.4" fill="none"/><path d="M5 8.7l2.5 2.5 4.5-5" stroke="#2aa8e8" stroke-width="1.6" fill="none"/></svg>implementing a solution<br>to improve</div>
  <div class="btn btn-blue" style="left:675px;top:2301px;width:134px;height:32px">Read More</div>
  <div class="btn btn-outline" style="left:822px;top:2301px;width:135px;height:32px">Get Started</div>
</section>

<section>
  <h2 class="abs center" style="left:0;top:2546px;width:1200px;font-size:38px;line-height:45px;font-weight:500;color:var(--navy);letter-spacing:.5px">Quality Improvement Software<br>for healthcare agencies</h2>
  <div class="photo video" role="img" aria-label="Hands holding printed analytics reports over a desk"></div>
  <svg class="abs" style="left:559px;top:2850px" width="94" height="94" viewBox="0 0 94 94"><circle cx="47" cy="47" r="47" fill="#e51b23"/><path d="M37 28v38l31-19z" fill="#fff"/></svg>
</section>

<section>
  <h2 class="abs center" style="left:0;top:3168px;width:1200px;font-size:38px;font-weight:500;color:var(--navy);letter-spacing:.5px">Our Happy Customers</h2>
  <div class="card quote-card" style="left:161px">
    <i class="quote-mark">“</i>
    <div style="display:flex;gap:14px;align-items:center"><div class="avatar" role="img" aria-label="Portrait of reviewer"></div><div><div style="font-size:13px">Mirela Stone</div><div style="font-size:10px;color:var(--muted)">Doctor</div></div></div>
    <p class="body-text" style="margin-top:18px">Lorem Ipsum is simply dummy text printing and typesetting industry simply dummy a ipsum is simply dummy.</p>
    <div class="stars" style="margin-top:20px">★★★★★</div>
  </div>
  <div class="card quote-card" style="left:465px">
    <i class="quote-mark">“</i>
    <div style="display:flex;gap:14px;align-items:center"><div class="avatar" role="img" aria-label="Portrait of reviewer"></div><div><div style="font-size:13px">Dorian Vale</div><div style="font-size:10px;color:var(--muted)">Doctor</div></div></div>
    <p class="body-text" style="margin-top:18px">Lorem Ipsum is simply dummy text printing and typesetting industry simply dummy a ipsum is simply dummy.</p>
    <div class="stars" style="margin-top:20px">★★★★★</div>
  </div>
  <div class="card quote-card" style="left:761px">
    <i class="quote-mark">“</i>
    <div style="display:flex;gap:14px;align-items:center"><div class="avatar" role="img" aria-label="Portrait of reviewer"></div><div><div style="font-size:13px">Liora Banks</div><div style="font-size:10px;color:var(--muted)">Doctor</div></div></div>
    <p class="body-text" style="margin-top:18px">Lorem Ipsum is simply dummy text printing and typesetting industry simply dummy a ipsum is simply dummy.</p>
    <div class="stars" style="margin-top:20px">★★★★★</div>
  </div>
  <div class="abs" style="left:538px;top:3513px;width:58px;height:3px;background:var(--blue)"></div>
  <div class="abs" style="left:602px;top:3513px;width:28px;height:3px;background:var(--navy)"></div>
  <div class="abs" style="left:638px;top:3513px;width:28px;height:3px;background:var(--navy)"></div>
</section>

<section>
  <h2 class="abs center" style="left:0;top:3586px;width:1200px;font-size:38px;font-weight:500;color:var(--navy)">Blog</h2>
  <article class="card blog-card" style="left:163px">
    <div class="photo blog-img" style="background:linear-gradient(135deg,#e6eef8,#7fa8e0 60%,#2a5bbf)" role="img" aria-label="Glasses and pen on printed bar charts"></div>
    <div class="date">12<br>DEC</div>
    <div class="abs" style="left:30px;top:226px;width:225px">
      <div style="font-size:13px;font-weight:500;color:var(--navy)">Blog Title Heading 01</div>
      <p class="body-text" style="margin-top:10px;font-size:10.5px">Lorem Ipsum is simply dummy text of the printing and typesetting industry. Lorem Ipsum has been the industry's...</p>
      <div style="margin-top:14px;font-size:10px;color:var(--blue)">READ MORE &gt;&gt;</div>
    </div>
  </article>
  <article class="card blog-card" style="left:462px">
    <div class="photo blog-img" style="background:linear-gradient(135deg,#d8dee6,#9aabbd 55%,#4d6a88)" role="img" aria-label="Doctor and nurse working on a laptop"></div>
    <div class="date">12<br>DEC</div>
    <div class="abs" style="left:30px;top:226px;width:225px">
      <div style="font-size:13px;font-weight:500;color:var(--navy)">Blog Title Heading 01</div>
      <p class="body-text" style="margin-top:10px;font-size:10.5px">Lorem Ipsum is simply dummy text of the printing and typesetting industry. Lorem Ipsum has been the industry's...</p>
      <div style="margin-top:14px;font-size:10px;color:var(--blue)">READ MORE &gt;&gt;</div>
    </div>
  </article>
  <article class="card blog-card" style="left:757px">
    <div class="photo blog-img" style="background:linear-gradient(135deg,#e8ddd0,#b99e86 50%,#4f79a8)" role="img" aria-label="Caregiver showing a tablet to an elderly woman"></div>
    <div class="date">12<br>DEC</div>
    <div class="abs" style="left:30px;top:226px;width:225px">
      <div style="font-size:13px;font-weight:500;color:var(--navy)">Blog Title Heading 01</div>
      <p class="body-text" style="margin-top:10px;font-size:10.5px">Lorem Ipsum is simply dummy text of the printing and typesetting industry. Lorem Ipsum has been the industry's...</p>
      <div style="margin-top:14px;font-size:10px;color:var(--blue)">READ MORE &gt;&gt;</div>
    </div>
  </article>
  <div class="btn" style="left:535px;top:4045px;width:134px;height:32px">View More</div>
</section>

<section>
  <h2 class="abs center" style="left:0;top:4118px;width:1200px;font-size:38px;font-weight:500;color:var(--navy)">Quick Contact</h2>
  <p class="abs center body-text" style="left:0;top:4172px;width:1200px">Lorem Ipsum is simply dummy text of the printing<br>and typesetting industry</p>
  <div class="field" style="left:348px;top:4225px;width:245px;height:30px">Name*</div>
  <div class="field" style="left:348px;top:4268px;width:245px;height:30px">Phone*</div>
  <div class="field" style="left:348px;top:4310px;width:245px;height:30px">Email*</div>
  <div class="field" style="left:607px;top:4225px;width:243px;height:115px">Message</div>
  <div class="btn" style="left:531px;top:4367px;width:144px;height:32px">Send</div>
</section>

<footer>
  <svg class="abs footer" viewBox="0 0 1200 337" preserveAspectRatio="none"><path d="M0 100C300 60 500 110 800 80S1100 20 1200 0V337H0Z" fill="#1c2d4e"/></svg>
  <div class="brand" style="left:146px;top:4600px;font-size:36px;color:var(--white)"><span class="brand-mark"></span>Veltrix820</div>
  <div class="abs foot-h" style="left:419px;top:4550px">Quick Links</div>
  <ul class="abs foot-list" style="left:419px;top:4586px">
    <li>›&nbsp; Home</li><li>›&nbsp; About us</li><li>›&nbsp; Our Services</li><li>›&nbsp; Features</li><li>›&nbsp; Blog</li><li>›&nbsp; Contact us</li>
  </ul>
  <div class="abs foot-h" style="left:580px;top:4550px">Contact Info</div>
  <ul class="abs foot-list" style="left:580px;top:4586px;line-height:22px">
    <li><svg width="10" height="12" viewBox="0 0 10 12" style="margin-right:12px"><path d="M5 11S1 7 1 4.5a4 4 0 0 1 8 0C9 7 5 11 5 11Z" stroke="#fff" fill="none"/><circle cx="5" cy="4.5" r="1.4" fill="#fff"/></svg>48 Harbor Lane,</li>
    <li style="padding-left:22px">Corvane City</li>
    <li style="padding-left:22px">TX 00000</li>
    <li><svg width="11" height="11" viewBox="0 0 11 11" style="margin-right:11px"><path d="M2 1h2l1 3-1.4 1a6 6 0 0 0 2.4 2.4L7 6l3 1v2a1 1 0 0 1-1 1A9 9 0 0 1 1 2a1 1 0 0 1 1-1Z" stroke="#fff" fill="none"/></svg>555 010 0199</li>
    <li><svg width="11" height="9" viewBox="0 0 11 9" style="margin-right:11px"><rect x=".5" y=".5" width="10" height="8" stroke="#fff" fill="none"/><path d="M.5 .5 5.5 5l5-4.5" stroke="#fff" fill="none"/></svg>info@veltrix820.com</li>
  </ul>
  <div class="abs foot-h" style="left:830px;top:4550px">Email Sign Up</div>
  <p class="abs body-text" style="left:830px;top:4590px;width:210px;color:var(--white);font-size:10.5px">Lorem Ipsum is simply dummy text of typesetting industry</p>
  <div class="abs" style="left:830px;top:4625px;width:206px;height:32px;border-radius:16px;background:var(--white);font-size:10px;color:#7a7f88;padding:9px 20px">Your Email</div>
  <div class="btn btn-blue" style="left:830px;top:4670px;width:206px;height:32px;font-size:12px">Submit</div>
  <div class="abs" style="left:161px;top:4780px;font-size:10px;color:var(--text)">Copyright © 2024 <b>Veltrix820</b>, All Rights Reserved.</div>
  <div class="social" style="left:908px"></div>
  <div class="social" style="left:942px;background:var(--navy)"></div>
  <div class="social" style="left:976px;background:var(--navy)"></div>
  <div class="social" style="left:1010px;background:var(--navy)"></div>
</footer>

</body>
</html>
```